draft # 94 and #95- Could we see the accent pink line in more of a brush stroke and could you make the logo a little bigger and the name and title smaller. Please add the website on the front of the card and add "Locally owned and operated" in the back.
draft #58
We would like to include our tag line of the front of the card "Making memories, one dip at a time!" Could we see this tagline in the same script font used in the logo. Could you also add
"Serving Bakersfield & Surrounding Areas" on the back of the card, above the watermark
Mossworks-Could we see the coordinating stationery and envelopes for draft #58
Thank you all for your submissions! We are off to a good start. Please show us more options using the chocolate brown as the primary color and using pink as the accent color. Also please remember to include "Locally owned and operated." on the back of the card. (without quotation marks, of course)
We would also like to see the fountain part of the logo or the initials as a watermark on the back of the card.
We want to make sure the font on the logo is bigger than the other font size used on the rest of the card.
Draft # 54 could we see the front logo a little bigger and add Locally owned and operated on the back.
Thanks!=)

```html
<!DOCTYPE html>
<html lang="en">
<head>
<meta charset="utf-8">
<title>Cocoa Lane Stationery Set</title>
<link href="https://fonts.googleapis.com/css2?family=Lato:wght@400;700&display=swap" rel="stylesheet">
<style>
:root{
  --brown:#4a1a18;
  --brown-dark:#3a1311;
  --pink:#e0245a;
  --paper:#ffffff;
  --bg:#ece6de;
  --ink:#3b2a28;
  --faint:rgba(74,26,24,.08);
}
*{box-sizing:border-box;margin:0;padding:0}
html,body{width:1200px;height:497px;overflow:hidden}
body{background:var(--bg);font-family:'Lato',sans-serif;color:var(--ink);position:relative}
.piece{position:absolute;background:var(--paper);box-shadow:0 2px 6px rgba(0,0,0,.25);overflow:hidden;border-radius:6px}
.piece svg.edge{position:absolute;inset:0;width:100%;height:100%}
.logo{position:absolute;display:flex;align-items:center;gap:5px;font-weight:700;color:var(--brown);white-space:nowrap}
.logo .dot{border-radius:50%;background:var(--brown)}
.logo.light{color:var(--paper)}
.logo.light .dot{background:var(--paper)}
.logo-box{position:absolute;background:var(--paper);border:1px solid var(--pink);display:flex;align-items:center;justify-content:center}
.contact{position:absolute;font-size:5px;line-height:1.5;color:var(--ink)}
.contact b{font-size:6px;display:block}
.tagline{position:absolute;font-size:5px;width:100%;text-align:center;color:var(--paper)}
.tagline.dark{color:var(--ink)}
.card{width:187px;height:113px}
.card.front{left:24px;top:67px}
.card.info{left:228px;top:67px}
.card.back-brown{left:24px;top:197px;background:var(--brown)}
.card.back-pink{left:228px;top:197px;background:var(--pink)}
.card.back-white{left:108px;top:322px;height:106px}
.letterhead{left:437px;top:24px;width:206px;height:451px;border-radius:0}
.watermark{position:absolute;left:40px;top:150px;display:flex;flex-direction:column;align-items:center;gap:6px;color:var(--faint);font-weight:700;font-size:22px}
.watermark .dot{width:70px;height:70px;border-radius:50%;background:var(--faint)}
.env{border-radius:2px}
.env.pink{left:876px;top:36px;width:300px;height:144px}
.env.plain{left:792px;top:132px;width:384px;height:136px}
.env.main{left:667px;top:192px;width:389px;height:276px}
</style>
</head>
<body>

<!-- Business card: front -->
<div class="piece card front">
  <svg class="edge" viewBox="0 0 187 113" preserveAspectRatio="none">
    <path d="M0 0H70Q30 10 0 60Z" fill="var(--brown)"/>
    <path d="M187 113H120Q160 100 187 50Z" fill="var(--brown)"/>
    <path d="M0 60Q30 12 70 0" fill="none" stroke="var(--pink)" stroke-width="2"/>
  </svg>
  <div class="logo" style="left:48px;top:42px;font-size:15px"><span class="dot" style="width:12px;height:12px"></span>Cocoa Lane</div>
  <div class="tagline dark" style="top:72px">Making memories, one dip at a time!</div>
</div>

<!-- Business card: contact side -->
<div class="piece card info">
  <svg class="edge" viewBox="0 0 187 113" preserveAspectRatio="none">
    <path d="M0 0H70Q30 10 0 60Z" fill="var(--brown)"/>
    <path d="M187 113H120Q160 100 187 50Z" fill="var(--brown)"/>
  </svg>
  <div class="logo-box" style="left:90px;top:14px;width:86px;height:34px">
    <div class="logo" style="position:static;font-size:10px"><span class="dot" style="width:8px;height:8px"></span>Cocoa Lane</div>
  </div>
  <div class="contact" style="left:14px;top:58px"><b>Dana Marlow</b>Owner</div>
  <div class="contact" style="left:96px;top:56px">Ph: 555 010 2200<br>Cell: 555 010 2201<br>Fax: 555 010 2202<br>mail@cocoalane.example<br>www.cocoalane.example</div>
</div>

<!-- Business card: brown back -->
<div class="piece card back-brown">
  <svg class="edge" viewBox="0 0 187 113" preserveAspectRatio="none">
    <path d="M187 0V55Q150 20 110 0Z" fill="var(--brown-dark)"/>
  </svg>
  <div class="logo-box" style="left:48px;top:28px;width:90px;height:42px;background:transparent;border:none">
    <div class="logo light" style="position:static;font-size:13px"><span class="dot" style="width:10px;height:10px"></span>Cocoa Lane</div>
  </div>
  <div class="tagline" style="top:92px">Locally owned and operated</div>
</div>

<!-- Business card: pink back -->
<div class="piece card back-pink">
  <div class="logo-box" style="left:44px;top:26px;width:98px;height:44px">
    <div class="logo" style="position:static;font-size:13px"><span class="dot" style="width:10px;height:10px"></span>Cocoa Lane</div>
  </div>
  <div class="tagline" style="top:90px">Locally owned and operated</div>
</div>

<!-- Business card: white back -->
<div class="piece card back-white">
  <div class="logo" style="left:50px;top:34px;font-size:14px"><span class="dot" style="width:11px;height:11px"></span>Cocoa Lane</div>
  <div class="tagline dark" style="top:86px">Locally owned and operated</div>
</div>

<!-- Letterhead -->
<div class="piece letterhead">
  <svg class="edge" viewBox="0 0 206 451" preserveAspectRatio="none">
    <path d="M0 0H45Q15 15 0 50Z" fill="var(--brown)"/>
    <path d="M206 451H150Q190 430 206 390Z" fill="var(--brown)"/>
    <path d="M0 50Q15 15 45 0" fill="none" stroke="var(--pink)" stroke-width="2"/>
  </svg>
  <div class="logo-box" style="left:36px;top:22px;width:80px;height:34px">
    <div class="logo" style="position:static;font-size:10px"><span class="dot" style="width:8px;height:8px"></span>Cocoa Lane</div>
  </div>
  <div class="contact" style="left:132px;top:18px">Ph: 555 010 2200<br>Fax: 555 010 2202<br>mail@cocoalane.example<br>www.cocoalane.example</div>
  <div class="watermark" role="img" aria-label="Faint brand watermark"><span class="dot"></span>Cocoa Lane</div>
</div>

<!-- Envelope with pink flap -->
<div class="piece env pink">
  <svg class="edge" viewBox="0 0 300 144" preserveAspectRatio="none">
    <path d="M0 0H300V30L150 85L0 30Z" fill="var(--pink)"/>
  </svg>
  <div class="logo-box" style="left:110px;top:18px;width:80px;height:30px">
    <div class="logo" style="position:static;font-size:9px"><span class="dot" style="width:7px;height:7px"></span>Cocoa Lane</div>
  </div>
</div>

<!-- Plain envelope -->
<div class="piece env plain">
  <div class="logo" style="left:250px;top:24px;font-size:10px"><span class="dot" style="width:8px;height:8px"></span>Cocoa Lane</div>
</div>

<!-- Main envelope front -->
<div class="piece env main">
  <svg class="edge" viewBox="0 0 389 276" preserveAspectRatio="none">
    <path d="M0 0H389V40Q200 -10 0 80Z" fill="var(--brown)"/>
    <path d="M0 84Q200 -6 389 44" fill="none" stroke="var(--pink)" stroke-width="3"/>
    <path d="M389 276H300Q360 260 389 220Z" fill="var(--brown)"/>
  </svg>
  <div class="logo-box" style="left:20px;top:58px;width:96px;height:38px">
    <div class="logo" style="position:static;font-size:11px"><span class="dot" style="width:9px;height:9px"></span>Cocoa Lane</div>
  </div>
  <div class="contact" style="left:24px;top:110px">Ph: 555 010 2200<br>Fax: 555 010 2202<br>mail@cocoalane.example</div>
</div>

</body>
</html>
```